Out Door Living brochure

We need a Great looking brochure to feature the latest in out door living. Showcasing out doors is the new living space.

I'm enclosing our logo and a brochure we had done recently it didn't have enough impact. This one was a single fold you can also provide a tri fold if you see fit. We like the verbiage, but if you can spice it up we would love to see that. This brochure will be added to our sales packet.
Thank you!!!

Target Market(s)

Home owners

Industry/Entity Type

Construction Company

Logo Text

(See logo) Beautiful Homes Built to Last Introducing Outdoor living 2017

Font styles to use
Serif

Requirements
Must have
• Logo and
• Beautiful Homes Built to Last
• Introducing Outdoor living 2017
Nice to have
• Benefits of outdoor living
Should not have
• Bad photos if these don't work let me know we can get others to replace the sapce

```html
<!DOCTYPE html>
<html lang="en">
<head>
<meta charset="utf-8">
<title>Outdoor Living 2017 Tri-fold Brochure</title>
<link href="https://fonts.googleapis.com/css2?family=Jost:wght@400;500;600;700&display=swap" rel="stylesheet">
<style>
  :root{
    --backdrop:#b9bcbf;
    --paper:#ffffff;
    --mist:#e6e8eb;
    --slate:#4f6b80;
    --slate-deep:#42596b;
    --sky:#5aaee0;
    --charcoal:#3b3e42;
    --ink:#3a3f45;
    --body:#5d6b78;
    --white:#ffffff;
  }
  *{box-sizing:border-box;margin:0;padding:0}
  html,body{width:826px;height:1200px;overflow:hidden}
  body{background:var(--backdrop);font-family:"Jost",sans-serif;position:relative}
  .brochure{position:absolute;left:20px;top:297px;width:786px;height:606px;display:flex;box-shadow:0 6px 18px rgba(0,0,0,.25)}
  .panel{position:relative;width:262px;height:606px;overflow:hidden}
  .footer-bar{position:absolute;left:0;bottom:0;width:100%;height:24px;background:var(--charcoal);color:var(--white);font-size:14px;letter-spacing:.3px;text-align:center;line-height:24px}

  /* About panel */
  .about{background:var(--mist)}
  .about-top{position:absolute;left:0;top:0;width:100%;height:325px;background:var(--paper)}
  .section-rule{position:absolute;top:22px;left:18px;right:18px;display:flex;align-items:center;gap:6px;font-size:19px;font-weight:500;letter-spacing:1.5px;color:var(--ink)}
  .section-rule::before,.section-rule::after{content:"";flex:1;height:1px;background:var(--ink)}
  .portrait{position:absolute;left:35px;top:59px;width:192px;height:192px;border-radius:50%;border:5px solid #4a4d52;background:radial-gradient(circle at 50% 45%,#c49a7c 0,#8a6a52 45%,#4d4038 75%,#2c3440 100%)}
  .caption{position:absolute;top:268px;left:10px;right:10px;text-align:center;font-size:10.5px;line-height:13px;color:var(--ink)}
  .about-copy{position:absolute;left:20px;right:14px;top:372px;font-size:12.5px;line-height:17px;color:var(--body)}
  .about-copy p+p{margin-top:15px}
  .about-copy .dark{color:var(--ink)}

  /* Contact panel */
  .contact{background:var(--slate)}
  .water-scene{position:absolute;inset:0;background:linear-gradient(180deg,#6f93b3 0%,#5f849f 30%,#56768d 55%,#4f6b80 75%)}
  .wordmark{position:absolute;left:0;right:0;text-align:center;color:var(--white);display:flex;flex-direction:column;align-items:center;gap:8px}
  .wordmark .mark{width:30px;height:30px;border-radius:50%;background:var(--white)}
  .wordmark .name{font-size:10.5px;font-weight:500;letter-spacing:.5px}
  .contact .wordmark{top:268px}
  .contact-title{position:absolute;top:352px;left:0;right:0;text-align:center;color:var(--sky);font-size:19px;font-weight:600;letter-spacing:.5px}
  .contact-item{position:absolute;left:0;right:0;text-align:center;color:var(--white)}
  .contact-item svg{display:block;margin:0 auto 6px}
  .phone{top:384px;font-size:14.5px;font-weight:500;letter-spacing:.5px}
  .address{top:438px;font-size:10px;line-height:13px}
  .email{top:518px;font-size:10px}
  .contact .footer-bar{background:var(--sky)}

  /* Cover panel */
  .cover{background:var(--mist)}
  .patio-photo{position:absolute;left:0;top:0;width:100%;height:323px;background:linear-gradient(180deg,#5b9fde 0%,#9cc3e6 35%,#6e7f8c 60%,#55636e 100%)}
  .cover .wordmark{top:22px}
  .tagline{position:absolute;left:0;top:323px;width:100%;height:85px;background:var(--slate);text-align:center;padding-top:18px;font-size:19px;font-weight:600;line-height:25px;letter-spacing:.3px;color:var(--white)}
  .tagline span{color:var(--sky)}
  .headline{position:absolute;left:0;right:0;top:428px;text-align:center;font-weight:600;color:var(--ink);font-size:29px;line-height:37px;letter-spacing:.5px}
  .headline .accent{color:var(--sky);font-size:38px;font-weight:700}
</style>
</head>
<body>
  <main class="brochure">
    <section class="panel about">
      <div class="about-top">
        <h2 class="section-rule">ABOUT US</h2>
        <div class="portrait" role="img" aria-label="Portrait photo of the general contractor"></div>
        <p class="caption">General Contractor Dan Ellery<br>of Harborline Builders in Bayview, CA</p>
      </div>
      <div class="about-copy">
        <p>When it comes building or remodeling your home, only the best will do. Superior quality home construction happens with experts guiding the building process.</p>
        <p>General Contractor Dan Ellery of Harborline Builders in Bayview <span class="dark">has a well-earned reputation of helping homeowners realize their dream home.</span></p>
      </div>
      <div class="footer-bar">www.harborlinebuilders.com</div>
    </section>

    <section class="panel contact">
      <div class="water-scene" role="img" aria-label="Photo of a lakeside view with palm tree under a blue overlay"></div>
      <div class="wordmark"><span class="mark"></span><span class="name">HARBORLINE BUILDERS</span></div>
      <h2 class="contact-title">CONTACT US</h2>
      <div class="contact-item phone">
        <svg width="16" height="16" viewBox="0 0 16 16"><circle cx="8" cy="8" r="7" fill="none" stroke="#5aaee0" stroke-width="1.2"/><path d="M5.5 4.5l1.3 0 .6 1.6-.8.7a5 5 0 0 0 2.6 2.6l.7-.8 1.6.6v1.3c-3.5.2-6.2-2.5-6-6z" fill="#5aaee0"/></svg>
        (555)-014-2290
      </div>
      <div class="contact-item address">
        <svg width="16" height="16" viewBox="0 0 16 16"><circle cx="8" cy="8" r="7" fill="none" stroke="#5aaee0" stroke-width="1.2"/><path d="M8 4a2.5 2.5 0 0 0-2.5 2.5C5.5 8.5 8 12 8 12s2.5-3.5 2.5-5.5A2.5 2.5 0 0 0 8 4z" fill="#5aaee0"/><circle cx="8" cy="6.5" r=".9" fill="#4f6b80"/></svg>
        Harborline Builders,<br>1450 Marina Vista Ave.,<br>Bayview, CA 94000
      </div>
      <div class="contact-item email">
        <svg width="16" height="16" viewBox="0 0 16 16"><circle cx="8" cy="8" r="7" fill="none" stroke="#5aaee0" stroke-width="1.2"/><rect x="4.5" y="5.5" width="7" height="5" fill="#5aaee0"/><path d="M4.5 5.5l3.5 2.7 3.5-2.7" fill="none" stroke="#4f6b80" stroke-width=".8"/></svg>
        dan@harborlinebuilders.com
      </div>
      <div class="footer-bar">www.harborlinebuilders.com</div>
    </section>

    <section class="panel cover">
      <div class="patio-photo" role="img" aria-label="Photo of a covered outdoor kitchen and patio under blue sky"></div>
      <div class="wordmark"><span class="mark"></span><span class="name">HARBORLINE BUILDERS</span></div>
      <p class="tagline">BEAUTIFUL HOMES<br><span>BUILT TO LAST</span></p>
      <h1 class="headline">INTRODUCING<br><span class="accent">OUTDOOR</span><br>LIVING 2017</h1>
      <div class="footer-bar">www.harborlinebuilders.com</div>
    </section>
  </main>
</body>
</html>
```